Nutrition business needs logo & business card design

We need a business card & logo design for a new company based in Toronto, Ontario Canada called Verdel Wellcraft.

We provide nutrition service using metrics as guide to manage client's progress. Our service creates individualized nutrition and lifestyle strategies that focuses on improving Performance, Longevity and Weight Loss. I would like to see designs that use the color of green, gray, blue and white.

The final design should:

--convey a feeling of connectedness with positive transformation.

-- communicate the idea of awareness with guided effort that yields personal independence for a better and more productive life

Target Market(s)

Professionals who work in the IT/Computer/Engineering/Banking industry specifically Directors, Managers, CEO's.

Industry/Entity Type

Health And Wellness

Contact Information for Business Card

Domric Hale, Owner
email: DHALE@verdelwellcraft.example
tel: - 555-274-9038

Logo Text

better health through analytics or measure to manage

Font styles to use
Other font styles liked:
• Garamound

Colors
ffffff
abd037
85acd3
757575
34a7d7

Requirements
Must have
• Good contrast and decent size font - ease of readability, aesthetically nice colors
Nice to have
• image of chart or graph that conveys measurement or analytics
Should not have
• Borders, images of food,

```html
<!DOCTYPE html>
<html lang="en">
<head>
<meta charset="utf-8">
<title>Verdel Wellcraft – Business Card</title>
<link rel="stylesheet" href="https://fonts.googleapis.com/css2?family=Open+Sans:wght@400;600&display=swap">
<style>
  :root {
    --backdrop: #2c2e33;
    --card: #ffffff;
    --brand-blue: #1a8cf0;
    --brand-green: #3aaa1e;
    --ink: #1f1f1f;
  }
  * { box-sizing: border-box; margin: 0; padding: 0; }
  html, body {
    width: 1200px;
    height: 864px;
    overflow: hidden;
    background: var(--backdrop);
    font-family: "Open Sans", sans-serif;
  }
  .card {
    position: absolute;
    left: 320px;
    width: 560px;
    height: 320px;
    background: var(--card);
    overflow: hidden;
    box-shadow: 0 10px 30px rgba(0,0,0,.35);
  }
  .card--front { top: 60px; }
  .card--back { top: 470px; }

  /* Front */
  .front-mark {
    position: absolute;
    left: 50%;
    top: 48px;
    width: 120px;
    height: 120px;
    margin-left: -60px;
    border-radius: 50%;
    border: 8px solid var(--brand-blue);
  }
  .front-name {
    position: absolute;
    left: 0;
    right: 0;
    top: 188px;
    text-align: center;
    font-size: 44px;
    font-weight: 400;
    letter-spacing: -0.5px;
    color: var(--brand-blue);
    white-space: nowrap;
  }

  /* Back */
  .back-name {
    position: absolute;
    left: 28px;
    top: 16px;
    font-size: 48px;
    font-weight: 400;
    letter-spacing: -0.5px;
    color: var(--brand-blue);
    white-space: nowrap;
  }
  .contact {
    position: absolute;
    left: 44px;
    top: 116px;
    color: var(--ink);
  }
  .contact__name {
    font-size: 19px;
    font-weight: 600;
    color: var(--brand-green);
    line-height: 1.1;
  }
  .contact__role {
    font-size: 14px;
    line-height: 1.3;
    margin-bottom: 14px;
  }
  .contact__address {
    font-size: 15px;
    line-height: 1.35;
    margin-bottom: 10px;
  }
  .contact__line {
    display: flex;
    align-items: center;
    gap: 10px;
    font-size: 15px;
    line-height: 1.5;
    white-space: nowrap;
  }
  .contact__icon { width: 12px; height: 12px; flex: none; }
  .contact__icon--fill { fill: var(--brand-green); }
  .contact__icon--stroke { fill: none; stroke: var(--brand-green); stroke-width: 2.5; stroke-linejoin: round; stroke-linecap: round; }
</style>
</head>
<body>
  <section class="card card--front">
    <div class="front-mark"></div>
    <div class="front-name">Verdel Wellcraft</div>
  </section>

  <section class="card card--back">
    <div class="back-name">Verdel Wellcraft</div>
    <div class="contact">
      <div class="contact__name">Domric Hale</div>
      <div class="contact__role">Managing Director</div>
      <div class="contact__address">220 Fenwick Lane, Suite 4<br>Toronto, ON M4B 2K7.</div>
      <div class="contact__line">
        <svg class="contact__icon contact__icon--fill" viewBox="0 0 24 24" aria-hidden="true"><path d="M6.6 10.8a15 15 0 0 0 6.6 6.6l2.2-2.2a1 1 0 0 1 1-.25 11.4 11.4 0 0 0 3.6.57 1 1 0 0 1 1 1V20a1 1 0 0 1-1 1A17 17 0 0 1 3 4a1 1 0 0 1 1-1h3.5a1 1 0 0 1 1 1c0 1.25.2 2.45.57 3.57a1 1 0 0 1-.25 1z"/></svg>
        <span>555-274-9038</span>
      </div>
      <div class="contact__line">
        <svg class="contact__icon contact__icon--stroke" viewBox="0 0 24 24" aria-hidden="true"><rect x="2" y="5" width="20" height="14" rx="1"/><path d="M2 6l10 7 10-7"/></svg>
        <span>DHALE@verdelwellcraft.example</span>
      </div>
      <div class="contact__line">
        <svg class="contact__icon contact__icon--stroke" viewBox="0 0 24 24" aria-hidden="true"><path d="M10 14a4 4 0 0 1 0-5.7l3-3a4 4 0 0 1 5.7 5.7l-1.5 1.5"/><path d="M14 10a4 4 0 0 1 0 5.7l-3 3a4 4 0 0 1-5.7-5.7l1.5-1.5"/></svg>
        <span>www.verdelwellcraft.example</span>
      </div>
    </div>
  </section>
</body>
</html>
```